Velmorant Entertainment
Official Website: www.velmorantentertainment.example
Facebook: www.socialpage.example/velmorantent
Past Posters: https://www.socialpage.example/media/set/?set=a.902846153027741.583920.640275913582016&;type=3

We are looking to design a high quality poster for our upcoming event which is NYE Masquerade Lantern Soiree (Velvet Night Edition). I need creative designers who can come up with good designs.

Please look at our past flyers to understand the quality of the work. Please dont waste your time if you know you will not be able to meet the standards. We can assure you guaranteed future projects.

What do we need?

1.. Timeline Picture using the image provided.
2. Flyer (which will be modified as required after initial design is approved)

Note: We will also require psd versions of both flyers once the design is approved. Further modifications will be required e.g Text, logos to be added and any other if chosen.

Here is a link of our past event posters, please have a look before designing anything:

https://www.socialpage.example/pg/VelmorantEnt/photos/?tab=album&album_id=902846153027741

Here are some posters that inspire us for a similar event, however, we need it to look more bollywood with a Bollywood actor and actress styled up in a black tie and cocktail dress.

1. https://templatemarket.example/item/item-one/50381726?s_rank=3
2. https://templatemarket.example/item/item-two/61749283?s_rank=15
3. https://templatemarket.example/item/item-three/7382915?s_rank=2
4. https://templatemarket.example/item/item-four/3650418?s_rank=22

Images that you can use or find similar ones:

1. https://www.pixelvaultimg.example/uploads/2015/07/actor-photo-3840x2160.jpg
2. https://www.imagefinder.example/imgres?imgurl=http%3A%2F%2Fstarglimpse.example%2Fuploads%2Factress-pics-07.jpg&w=900&h=1149

We require an elegant NYE Bollywood Party poster with the following information:

VELMORANT ENTERTAINMENT & SAFFRONDALE RESTAURANT
PRESENTS

NYE MASQUERADE LANTERN SOIREE (make an AMAZING logo/style font)
Velvet Night Edition (make an AMAZING logo/style font)
Feat. DJ KORU (Sydney)
BOLLYWOOD • ELECTRO • URBAN BHANGRA • COMMERCIAL TOP 40 • DANCE

31st DECEMBER 2018 | 9.00 PM ON WARDS

DRESS CODE: BLACK TIE & COCKTAIL DRESSES

$50 GENERAL
$99 VVIP - includes (BOTTLE SERVICE, HOSTS, LIMITED CAPACITY VIP SECTION, UNLIMITED TAP BEER & SELECTED WINE UNTIL 11.00PM)
TICKET INCLUDES: ENTRY, SELECTED FINGER FOODS & CHAATS (UNTIL 11.00 PM) & GLASS OF CHAMPAGNE

FOR TICKETING, SPONSORSHIP OF GENERAL ENQUIRIES, PLEASE CONTACT:
MIRESH KANTOLE 0458 261 947 l TOSHAN MELURI 0466 174 852

BOOK ONLINE AT WWW.VELMORANTENTERTAINMENT.EXAMPLE

DOORS OPEN 9.00 PM l VALID PHOTO ID REQUIRED FOR ENTRY l 18+ EVENT

--------------------------------------------------------------------------------------------------------------------------

```html
<!DOCTYPE html>
<html lang="en">
<head>
<meta charset="utf-8">
<title>NYE Masquerade Lantern Soiree – Velvet Night Edition</title>
<link rel="stylesheet" href="https://fonts.googleapis.com/css2?family=Cinzel:wght@400;700&family=Cinzel+Decorative:wght@700;900&family=Oswald:wght@500;600&family=Montserrat:wght@500;600;700&family=Playfair+Display:wght@700&display=swap">
<style>
  :root {
    --page-bg: #f1f1f1;
    --ink: #050302;
    --gold: #e9b94a;
    --gold-light: #ffd978;
    --gold-deep: #b37a1e;
    --flare: #f08a1c;
    --white: #ffffff;
    --band: #f3c33e;
  }
  * { box-sizing: border-box; margin: 0; padding: 0; }
  html, body { width: 1035px; height: 1200px; overflow: hidden; background: var(--page-bg); }
  .flyer {
    position: absolute; left: 93px; top: 0; width: 848px; height: 1200px; overflow: hidden;
    background:
      radial-gradient(ellipse 340px 260px at 430px 300px, rgba(240,138,28,.55), transparent 70%),
      radial-gradient(ellipse 620px 180px at 424px 520px, rgba(200,100,20,.35), transparent 70%),
      radial-gradient(ellipse 500px 420px at 424px 360px, rgba(90,40,5,.6), transparent 75%),
      var(--ink);
    font-family: "Montserrat", sans-serif;
    text-align: center;
  }
  .abs { position: absolute; left: 0; width: 100%; }
  .presenter { top: 18px; font-family: "Cinzel", serif; font-weight: 700; color: var(--gold); font-size: 18px; letter-spacing: .5px; }
  .partners { top: 46px; font-family: "Cinzel", serif; font-weight: 700; color: var(--gold); font-size: 17px; }
  .partners small { font-size: 12px; }
  .presents { top: 76px; font-family: "Playfair Display", serif; font-style: italic; color: var(--white); font-size: 15px; z-index: 2; }
  .hero-photo {
    position: absolute; left: 160px; top: 102px; width: 490px; height: 420px;
    background:
      linear-gradient(90deg, rgba(20,20,24,.95) 0 48%, rgba(200,70,40,.75) 60% 80%, transparent 100%),
      radial-gradient(ellipse at 50% 40%, rgba(255,170,60,.35), transparent 70%);
    border-radius: 40% 40% 6% 6% / 30% 30% 6% 6%;
    opacity: .9;
  }
  .title-nye { top: 450px; font-family: "Cinzel Decorative", serif; font-weight: 900; font-size: 150px; line-height: 1; color: var(--gold); letter-spacing: 4px;
    background: linear-gradient(180deg, var(--gold-light), var(--gold) 55%, var(--gold-deep)); -webkit-background-clip: text; background-clip: text; -webkit-text-fill-color: transparent; }
  .title-line { font-family: "Cinzel", serif; font-weight: 700; font-size: 50px; line-height: 1; color: var(--gold); }
  .title-line.one { top: 612px; }
  .title-line.two { top: 666px; }
  .edition { top: 725px; font-family: "Montserrat", sans-serif; font-weight: 600; font-size: 19px; letter-spacing: 7px; color: var(--white); }
  .featuring { top: 764px; display: flex; justify-content: center; align-items: center; gap: 14px; }
  .featuring .rule { width: 110px; height: 2px; background: linear-gradient(90deg, transparent, var(--gold)); }
  .featuring .rule.right { background: linear-gradient(90deg, var(--gold), transparent); }
  .featuring .feat { font-family: "Playfair Display", serif; font-style: italic; color: var(--gold); font-size: 22px; }
  .featuring .dj { font-family: "Oswald", sans-serif; font-weight: 600; color: var(--gold); font-size: 40px; letter-spacing: 1px; }
  .genres { top: 824px; font-family: "Oswald", sans-serif; font-weight: 500; font-size: 21px; color: var(--gold); }
  .date { top: 860px; font-family: "Playfair Display", serif; font-weight: 700; font-size: 40px; color: var(--gold); }
  .date sup { font-size: 22px; }
  .entry { top: 920px; display: flex; justify-content: center; align-items: center; gap: 22px; font-family: "Montserrat", sans-serif; font-weight: 600; font-size: 18px; color: var(--white); }
  .dress-code { display: flex; border: 2px solid var(--gold); font-family: "Playfair Display", serif; font-size: 15px; }
  .dress-code b { background: var(--ink); color: var(--white); padding: 4px 8px; }
  .dress-code span { background: var(--gold); color: var(--ink); padding: 4px 14px; font-weight: 700; }
  .divider { top: 966px; left: 20px; width: 808px; border-top: 2px dashed rgba(233,185,74,.55); }
  .ticket { position: absolute; left: 22px; display: flex; align-items: center; gap: 14px; text-align: left; }
  .ticket .price { flex-shrink: 0; font-family: "Oswald", sans-serif; font-weight: 600; color: var(--gold); font-size: 32px; line-height: 1; white-space: nowrap; }
  .ticket .detail { font-family: "Montserrat", sans-serif; font-weight: 700; color: var(--gold); font-size: 13px; line-height: 1.3; white-space: nowrap; }
  .ticket.general { top: 984px; }
  .ticket.vvip { top: 1032px; }
  .age-badge { position: absolute; left: 712px; top: 975px; width: 114px; height: 114px; border-radius: 50%;
    background: radial-gradient(circle at 40% 35%, var(--gold-light), var(--gold) 55%, var(--gold-deep));
    display: flex; flex-direction: column; justify-content: center; color: var(--ink); font-family: "Montserrat", sans-serif; font-weight: 700; line-height: 1.05; }
  .age-badge .age { font-size: 30px; }
  .age-badge .label { font-size: 15px; }
  .age-badge .note { font-size: 10px; }
  .contact { top: 1098px; font-family: "Montserrat", sans-serif; font-weight: 600; font-size: 15px; line-height: 1.45; color: var(--white); }
  .contact .lead { color: var(--gold); }
  .booking-band { position: absolute; left: 0; bottom: 0; width: 100%; height: 50px; background: linear-gradient(180deg, var(--gold-light), var(--band)); display: flex; align-items: center; justify-content: center;
    font-family: "Oswald", sans-serif; font-weight: 600; font-size: 23px; color: var(--ink); }
</style>
</head>
<body>
  <main class="flyer">
    <p class="abs presenter">SWIFTPATH MIGRATION AUSTRALIA</p>
    <p class="abs partners"><small>IN ASSOCIATION WITH</small> VELMORANT ENTERTAINMENT &amp; SAFFRONDALE RESTAURANT</p>
    <p class="abs presents">Presents</p>

    <div class="hero-photo" role="img" aria-label="Photo of an actor in a black tuxedo and an actress in a red cocktail dress against golden light flares"></div>

    <h1 class="abs title-nye">NYE</h1>
    <p class="abs title-line one">MASQUERADE</p>
    <p class="abs title-line two">LANTERN SOIREE</p>
    <p class="abs edition">VELVET NIGHT EDITION</p>

    <div class="abs featuring">
      <span class="rule"></span>
      <span class="feat">Feat.</span>
      <span class="dj">DJ KORU</span>
      <span class="rule right"></span>
    </div>

    <p class="abs genres">BOLLYWOOD | ELECTRO | URBAN BHANGRA | COMMERCIAL TOP 40 | DANCE</p>
    <p class="abs date">31<sup>ST</sup> DECEMBER 2018</p>

    <div class="abs entry">
      <span class="doors">DOORS OPEN 9.00 PM</span>
      <div class="dress-code"><b>DRESS CODE:</b><span>BLACK TIE &amp; COCKTAIL DRESSES</span></div>
    </div>

    <div class="abs divider"></div>

    <div class="ticket general">
      <span class="price">$50 GENERAL</span>
      <span class="detail">TICKET INCLUDES: ENTRY, SELECTED FINGER FOODS<br>&amp; CHAATS (UNTIL 11.00 PM) &amp; GLASS OF CHAMPAGNE</span>
    </div>
    <div class="ticket vvip">
      <span class="price">$99 VVIP</span>
      <span class="detail">ADDITIONS: BOTTLE SERVICE, HOSTS, LIMITED CAPACITY VIP<br>SECTION, UNLIMITED TAP BEER &amp; SELECTED WINE UNTIL 11.00PM)</span>
    </div>

    <div class="age-badge">
      <span class="age">18+</span>
      <span class="label">EVENT</span>
      <span class="note">PHOTO ID<br>REQUIRED</span>
    </div>

    <p class="abs contact"><span class="lead">FOR TICKETING, SPONSORSHIP OF GENERAL ENQUIRIES, PLEASE CONTACT:</span><br>MIRESH KANTOLE 0458 261 947 | TOSHAN MELURI 0466 174 852</p>

    <footer class="booking-band">BOOK ONLINE AT WWW.VELMORANTENTERTAINMENT.EXAMPLE</footer>
  </main>
</body>
</html>
```